VantorGoods.example -Ecommerce Website for Luxury Products

This will be an ecommerce site. A website portal that will allow both consumers to enter one way and see specific purchase options and businesses to enter via a different link that allows B2B to see their specific options once logged into. B2C can purchase both as a guest/or after account is setup. B2B must be approved to set up account. This is front end website project. Back-end integration is separate. Will be hosted on Servalia with a domain registration held at NetBrindle. Additional website concept/idea/synergy can be found from sister site-KRWMLodging.example

```html
<!DOCTYPE html>
<html lang="en">
<head>
<meta charset="utf-8">
<title>VantorGoods — Luxury Lifestyle Accoutrements</title>
<link rel="stylesheet" href="https://fonts.googleapis.com/css2?family=Playfair+Display:wght@400;500&family=Poppins:wght@300;400;500&display=swap">
<style>
:root{
  --bg:#0e0e0e;
  --bg-soft:#1a1a1a;
  --panel:#1c1c1c;
  --gold:#ab8a66;
  --gold-btn:#b8926c;
  --ink:#ffffff;
  --ink-soft:#d9d4cd;
  --ink-dark:#1b1b1b;
  --line:#4a4a4a;
  --serif:'Playfair Display', Georgia, serif;
  --sans:'Poppins', Arial, sans-serif;
}
*{box-sizing:border-box;margin:0;padding:0}
html,body{width:1200px;height:3270px;overflow:hidden}
body{
  position:relative;font-family:var(--sans);color:var(--ink);
  background:
    radial-gradient(ellipse 520px 380px at 600px 250px,#2b2b2b 0%,transparent 70%),
    radial-gradient(ellipse 500px 700px at 1200px 1000px,#262626 0%,transparent 70%),
    radial-gradient(ellipse 500px 600px at 0px 500px,#222 0%,transparent 70%),
    radial-gradient(ellipse 500px 500px at 1150px 2700px,#262626 0%,transparent 70%),
    var(--bg);
}
.abs{position:absolute}
.title{font-family:var(--serif);font-weight:400;color:var(--gold);text-align:center;text-transform:uppercase;letter-spacing:.5px}
.btn{position:absolute;display:flex;align-items:center;justify-content:center;border-radius:22px;font-size:10.5px;font-weight:500;text-transform:uppercase;letter-spacing:.2px}
.btn-gold{background:var(--gold-btn);color:var(--ink-dark)}
.btn-outline{border:1px solid #d8d8d8;color:var(--ink)}

/* nav */
.site-nav{left:147px;top:23px;width:906px;height:43px;background:#f8f7f3;border-radius:8px;display:flex;align-items:center;padding:0 20px 0 14px}
.brand{display:flex;align-items:center;gap:8px;color:#111}
.brand-dot{width:18px;height:18px;border-radius:50%;background:#111}
.brand-name{font-family:var(--serif);font-size:16px;letter-spacing:.5px}
.nav-links{margin-left:auto;display:flex;gap:24px;list-style:none;font-size:9.5px;color:#333;text-transform:uppercase}

/* hero */
.hero-title{left:0;top:208px;width:1200px;font-size:40px;line-height:44px}
.hero-sub{left:0;top:308px;width:1200px;text-align:center;font-size:12.5px;letter-spacing:.3px}
.photo{position:absolute;border-radius:22px;box-shadow:0 12px 30px rgba(0,0,0,.55)}
.photo-flatlay{left:232px;top:475px;width:222px;height:270px;transform:rotate(-14deg);background:linear-gradient(135deg,#d8d6d2,#8e8b86 60%,#3a3836)}
.photo-cigars{left:462px;top:440px;width:275px;height:332px;background:linear-gradient(160deg,#2c3a2a,#6e3f22 45%,#8a5532 70%,#3a2214)}
.photo-oils{left:745px;top:475px;width:222px;height:270px;transform:rotate(14deg);background:linear-gradient(150deg,#4a5a2c,#1e2a18 50%,#3b2a14)}

/* about */
.about-title{left:0;top:888px;width:1200px;font-size:36px}
.about-body{left:300px;top:948px;width:600px;text-align:center;font-size:11px;line-height:19.5px;color:var(--ink-soft)}

/* retail */
.retail-title{left:0;top:1128px;width:1200px;font-size:36px}
.tile{position:absolute;border-radius:18px;overflow:hidden}
.tile-cigar{left:18px;top:1219px;width:578px;height:455px;background:radial-gradient(ellipse at 65% 55%,#6b3a22,#3b2618 55%,#24180f)}
.tile-fragrance{left:608px;top:1219px;width:578px;height:221px;background:linear-gradient(90deg,#141414 40%,#4a3320 70%,#a07050 85%,#c89090)}
.tile-attire{left:608px;top:1453px;width:578px;height:221px;background:linear-gradient(90deg,#121212 35%,#2e2e2e 60%,#8a8a8a 85%,#4a4a4a)}
.tile-copy{position:absolute}
.tile-kicker{font-size:11.5px;color:var(--ink-soft)}
.tile-name{font-family:var(--serif);font-size:22px;color:var(--gold);text-transform:uppercase;margin:2px 0 6px}
.tile-desc{font-size:11.5px;line-height:16px;color:var(--ink-soft);width:220px}

/* wholesale */
.wholesale{left:18px;top:1689px;width:1168px;height:361px;border-radius:18px;background:radial-gradient(ellipse at 50% 40%,#5a3a22,#2e2016 55%,#17110c)}
.wholesale-title{left:0;top:1810px;width:1200px;text-align:center;font-family:var(--serif);font-size:38px;text-transform:uppercase}
.wholesale-body{left:300px;top:1860px;width:600px;text-align:center;font-size:11.5px;line-height:19.5px}

/* partners */
.partners-title{left:0;top:2136px;width:1200px;font-size:36px}
.partner{position:absolute;top:2214px;width:256px;height:281px;border-radius:16px;background:var(--panel)}
.partner-photo{position:absolute;left:6px;top:6px;width:244px;height:192px;border-radius:12px}
.partner-label{position:absolute;left:0;top:232px;width:100%;text-align:center;font-family:var(--serif)}
.partner-label small{display:block;font-size:10px;color:var(--gold)}
.partner-label span{font-size:13px}

/* contact */
.contact-title{left:0;top:2584px;width:1200px;font-size:36px}
.field{position:absolute;height:35px;border:1px solid var(--line);border-radius:16px;padding:11px 20px;font-size:10px;color:var(--ink-soft)}
.field-message{height:98px}

/* footer */
.site-footer{left:0;top:2940px;width:1200px;height:330px;background:var(--bg-soft);border-radius:28px 28px 0 0}
.footer-name{left:0;top:3056px;width:1200px;text-align:center;font-family:var(--serif);font-size:30px;letter-spacing:1.5px}
.footer-tag{left:0;top:3100px;width:1200px;text-align:center;font-size:9.5px;letter-spacing:2px;font-weight:500}
.footer-links{left:0;top:3128px;width:1200px;display:flex;justify-content:center;gap:23px;list-style:none;font-size:9.5px;color:var(--ink-soft)}
.social{position:absolute;top:3162px;width:23px;height:23px;border-radius:50%;background:#2c2c2c;border:1px solid #3c3c3c}
.footer-rule{left:147px;top:3230px;width:906px;height:1px;background:#3a3a3a}
.to-top{left:1058px;top:3216px;width:28px;height:28px;border-radius:50%;background:var(--gold-btn);display:flex;align-items:center;justify-content:center}
.copyright{left:0;top:3247px;width:1200px;text-align:center;font-size:9.5px;color:var(--ink-soft)}
</style>
</head>
<body>

<nav class="abs site-nav">
  <div class="brand"><span class="brand-dot"></span><span class="brand-name">VANTORGOODS</span></div>
  <ul class="nav-links">
    <li>About Us</li><li>Retail Collections</li><li>Wholesale Portal</li><li>Partner Showcase</li><li>Contact &amp; Concierge</li>
  </ul>
</nav>

<header>
  <h1 class="abs title hero-title">Purveyors of Luxury<br>Lifestyle Accoutrements</h1>
  <p class="abs hero-sub">CURATED FOR CONNOISSEURS. CRAFTED FOR LOUNGES.</p>
  <a class="btn btn-gold" style="left:414px;top:347px;width:148px;height:34px">Shop Retail Collections</a>
  <a class="btn btn-outline" style="left:603px;top:347px;width:184px;height:34px">Explore Wholesale Portal</a>
  <div class="photo photo-flatlay" role="img" aria-label="Flat lay of sunglasses, lipstick and leather accessories on patterned tile"></div>
  <div class="photo photo-oils" role="img" aria-label="Amber dropper bottles of oil among green leaves"></div>
  <div class="photo photo-cigars" role="img" aria-label="Bundle of cigars on a wooden humidor"></div>
</header>

<section>
  <h2 class="abs title about-title">About VantorGoods</h2>
  <p class="abs about-body">VantorGoods is a division of KRWM Lodging, dedicated to curating premium lifestyle products for both individual connoisseurs and sophisticated business partners. We deliver exclusivity, craftsmanship, and indulgence across our retail and wholesale offerings.</p>
  <a class="btn btn-gold" style="left:548px;top:1028px;width:104px;height:32px">Read More</a>
</section>

<section>
  <h2 class="abs title retail-title">Retail Collections</h2>
  <article class="tile tile-cigar" role="img" aria-label="Briar tobacco pipe beside a tin of loose tobacco">
    <div class="tile-copy" style="left:60px;top:190px">
      <p class="tile-kicker">Cigar Accessory</p>
      <h3 class="tile-name">Cigar Accessories</h3>
      <p class="tile-desc">Premium humidor essentials &amp; tools for the connoisseur.</p>
    </div>
  </article>
  <article class="tile tile-fragrance" role="img" aria-label="Amber fragrance bottle with pink roses on dark wood">
    <div class="tile-copy" style="left:58px;top:78px">
      <p class="tile-kicker">Luxury Fragrances</p>
      <h3 class="tile-name">Fragrances &amp; Oils</h3>
      <p class="tile-desc">Exclusive scents to elevate your personal style.</p>
    </div>
  </article>
  <article class="tile tile-attire" role="img" aria-label="Black dress shoes, bow tie, watch and cologne on a dark surface">
    <div class="tile-copy" style="left:57px;top:66px">
      <p class="tile-kicker">Luxury Attire</p>
      <h3 class="tile-name">Attire &amp; Accessories</h3>
      <p class="tile-desc">Crafted for refinement and sophistication.</p>
    </div>
  </article>
</section>

<section>
  <div class="abs wholesale" role="img" aria-label="Dimly lit lounge interior with leather sofas and a bar"></div>
  <h2 class="abs wholesale-title">Wholesale Portal</h2>
  <p class="abs wholesale-body">Licensed partners, lounge owners, and event organizers can apply for an approved account to access exclusive wholesale pricing and bulk products.</p>
  <a class="btn btn-gold" style="left:484px;top:1920px;width:145px;height:34px">Apply for Account</a>
  <a class="btn btn-outline" style="left:631px;top:1920px;width:87px;height:34px">Login</a>
</section>

<section>
  <h2 class="abs title partners-title">Partner Showcase</h2>
  <div class="partner" style="left:204px">
    <div class="partner-photo" role="img" aria-label="Cigar lounge with orange leather armchairs" style="background:linear-gradient(160deg,#3a2418,#8a4a24 55%,#2a1a10)"></div>
    <p class="partner-label"><small>Lounge 1</small><span>Amber Den, New York</span></p>
  </div>
  <div class="partner" style="left:471px">
    <div class="partner-photo" role="img" aria-label="Perfume bottles on a black leather box" style="background:linear-gradient(150deg,#2a3a2e,#1a1a1a 50%,#c0a070 80%,#e8e8e0)"></div>
    <p class="partner-label"><small>Lounge 2</small><span>Halcyon Lounge, Miami</span></p>
  </div>
  <div class="partner" style="left:740px">
    <div class="partner-photo" role="img" aria-label="Velvet lounge with rows of plush sofas" style="background:linear-gradient(170deg,#2a2018,#5a4634 50%,#1e1812)"></div>
    <p class="partner-label"><small>Lounge 3</small><span>Ember Room, Los Angeles</span></p>
  </div>
</section>

<section>
  <h2 class="abs title contact-title">Contact &amp; Concierge</h2>
  <form>
    <div class="field" style="left:373px;top:2652px;width:225px">Name</div>
    <div class="field" style="left:603px;top:2652px;width:224px">Email</div>
    <div class="field" style="left:373px;top:2695px;width:225px">Phone</div>
    <div class="field" style="left:603px;top:2695px;width:224px">Subject</div>
    <div class="field field-message" style="left:371px;top:2739px;width:456px">Message</div>
    <a class="btn btn-gold" style="left:552px;top:2845px;width:96px;height:32px">Submit Now</a>
  </form>
</section>

<footer>
  <div class="abs site-footer"></div>
  <p class="abs footer-name">VANTORGOODS</p>
  <p class="abs footer-tag">A DIVISION OF KRWM LODGING</p>
  <ul class="abs footer-links">
    <li>HOME</li><li>ABOUT US</li><li>RETAIL</li><li>WHOLESALE</li><li>PARTNERS</li><li>CONTACT</li>
  </ul>
  <span class="social" style="left:559px" aria-label="Social link"></span>
  <span class="social" style="left:589px" aria-label="Social link"></span>
  <span class="social" style="left:618px" aria-label="Social link"></span>
  <div class="abs footer-rule"></div>
  <a class="abs to-top" aria-label="Back to top"><svg width="10" height="10" viewBox="0 0 10 10"><path d="M2 6.5 5 3.5 8 6.5" fill="none" stroke="#1b1b1b" stroke-width="1.4"/></svg></a>
  <p class="abs copyright">© 2026 VantorGoods. All rights reserved.</p>
</footer>

</body>
</html>
```